Website creation for audiovisual activities

I want a website for my director of photography activity. It's primarily composed of screenshots in gallery format, followed by detailed pages for each production.

Here's my current website:
www.lionelbravat.example
I'd like a more modern and streamlined design, and for the site to be responsive on phones and computers. I also want to be able to easily add photos and text to it later.

Target Market(s)

productions society, directors and producers.

Industry/Entity Type

Audiovisual / TV

Coding

Coded - Design and coding required

Number of Pages Required

5+ page

Font styles to use
Sans Serif

Colors
0054AA
0677BA
7BADD7
CADEEF
E8F1F8
0094D4
00A9DD
6FCCEA
C7EBF8
E9F6FB
00AB8E
00BBA5
67D7C9
C6EFE9
E9F9F6
6B429C
8869AF
B7A5CE
E3DAEB
F3F0F8

Requirements
Must have
• a modern look with a photo gallery on the homepage
Nice to have
• a light background with large, dynamic images
Should not have
• a dark background and an overly classic look

```html
<!DOCTYPE html>
<html lang="en">
<head>
<meta charset="utf-8">
<title>Lionel Bravat — About</title>
<link href="https://fonts.googleapis.com/css2?family=Inter:wght@400;500&display=swap" rel="stylesheet">
<style>
:root{
  --blue-deep:#0054AA;
  --cyan:#0094D4;
  --teal:#00AB8E;
  --violet:#6B429C;
  --ink:#1a1a1a;
  --text-muted:#6b6b6b;
  --nav-muted:#6b6b6b;
  --line:#e6e6e6;
  --bg:#ffffff;
  --photo-a:#b9b5b1;
  --photo-b:#5d5a57;
}
*{margin:0;padding:0;box-sizing:border-box}
html,body{width:1200px;height:613px;overflow:hidden;background:var(--bg)}
body{position:relative;font-family:"Inter",sans-serif;color:var(--ink)}
.site-header{position:absolute;left:0;top:0;width:1200px;height:24px;border-bottom:1px solid var(--line)}
.brand{position:absolute;left:372px;top:6px;font-size:8.5px;font-weight:500;color:var(--blue-deep)}
.main-nav{position:absolute;left:711px;top:0;display:flex;gap:12.5px;height:24px}
.main-nav a{font-size:6.4px;color:var(--nav-muted);text-decoration:none;line-height:24px;position:relative}
.main-nav a.active{color:var(--blue-deep)}
.main-nav a.active::after{content:"";position:absolute;left:0;right:0;bottom:-1px;height:1px;background:var(--blue-deep)}
.portrait{position:absolute;left:420px;top:36px;width:133px;height:178px;border-radius:2px;background:linear-gradient(160deg,var(--photo-a),var(--photo-b))}
.about-title{position:absolute;left:571px;top:33px;font-size:19px;font-weight:400}
.about-copy{position:absolute;left:571px;top:67px;width:206px}
.about-copy p{font-size:7px;line-height:11px;color:var(--text-muted);margin-bottom:8.7px}
.about-copy p.lead{color:var(--ink)}
.section-title{position:absolute;left:420px;font-size:12px;font-weight:400}
.highlights-title{top:244px}
.clients-title{top:414px}
.highlights{position:absolute;left:420px;top:271px;list-style:none}
.highlight{height:23.5px;margin-bottom:6.5px;border-left:1px solid;padding-left:9px;padding-top:3.5px}
.highlight h3{font-size:6.1px;font-weight:400;line-height:8px}
.highlight p{font-size:5.2px;color:var(--text-muted);line-height:9px}
.h-blue{border-color:var(--blue-deep)}
.h-cyan{border-color:var(--cyan)}
.h-teal{border-color:var(--teal)}
.h-violet{border-color:var(--violet)}
.clients{position:absolute;left:420px;top:459px;width:360px;display:grid;grid-template-columns:repeat(3,114px);column-gap:9.5px;row-gap:9.4px}
.client{height:21.6px;border:1px solid var(--line);border-radius:2px;display:flex;align-items:center;justify-content:center;font-size:6.1px;font-weight:500}
</style>
</head>
<body>
<header class="site-header">
  <div class="brand">Lionel Bravat</div>
  <nav class="main-nav">
    <a href="#">Work</a>
    <a href="#" class="active">About</a>
    <a href="#">Showreel</a>
    <a href="#">Contact</a>
  </nav>
</header>

<div class="portrait" role="img" aria-label="Portrait of the cinematographer holding a cinema camera rig"></div>
<h1 class="about-title">About</h1>
<div class="about-copy">
  <p class="lead">Award-winning cinematographer with over 15 years of experience crafting visual stories for film, television, and commercial productions. Based between London and Los Angeles, working globally with directors and production companies.</p>
  <p>My approach combines technical precision with artistic vision, always in service of the story. I believe in the power of light, composition, and camera movement to create emotional resonance and visual poetry.</p>
  <p>Recent work includes feature films that premiered at Highpine and Lakeshore, Aurelia-nominated television series, and award-winning commercial campaigns for global brands.</p>
</div>

<h2 class="section-title highlights-title">Career Highlights</h2>
<ul class="highlights">
  <li class="highlight h-blue"><h3>Highpine Film Festival - Cinematography Award</h3><p>Best Cinematography, U.S. Dramatic Competition (2024)</p></li>
  <li class="highlight h-cyan"><h3>Aurelia Nomination</h3><p>Outstanding Cinematography for a Limited Series (2024)</p></li>
  <li class="highlight h-teal"><h3>Guild of Screen Cinematographers</h3><p>Best Cinematography in Television Drama (2023)</p></li>
  <li class="highlight h-violet"><h3>Harbour Lions</h3><p>Gold Anchor for Cinematography (2023)</p></li>
</ul>

<h2 class="section-title clients-title">Selected Clients</h2>
<div class="clients" style="top:441px">
  <div class="client">North Nine Studios</div>
  <div class="client">Vantage TV</div>
  <div class="client">Streamhouse</div>
  <div class="client">Orchard TV+</div>
  <div class="client">Lanternfield Pictures</div>
  <div class="client">Holt+Marrow</div>
  <div class="client">Albion Films</div>
  <div class="client">Keystone Features</div>
  <div class="client">Riverline Studios</div>
  <div class="client">Calder Bros.</div>
  <div class="client">Meridian Pictures</div>
  <div class="client">Paragon Pictures</div>
</div>
</body>
</html>
```